Web design for financial services

A modern web design of financial services (brokerage firm)
Req.s and technology tags :
- Very mobile friendly.
- One paged with some inner pages.
- Animated sticky header .
- Member login area for e-trade.
- Support RTL language.
- HTML & CSS.

The logo will be Home link
• OKDM :
WHO WE ARE
Content :
i) Board of Directors
ii) Mission Statement
iii) Corporate Values
iv) Regulations
• Financial Services :
WHAT WE DO
Content:
i) Electronic trading
ii) Trading desk
iii) Institutional
iv) Investors Education
• News
• Market Tools
• Forms---- opens new page
• Careers---- opens new page
• Contact Us----opens new page

The website is :
http://www.okdm-pelorn.com/

The logo need some changes to be more modern and impressively , but with keeping same structure .

Some related websites :
https://www.vu-markt.com/

Target Market(s)

financial market

Industry/Entity Type

Financial Service

Coding

Coded - Design and coding required

Number of Pages Required

2 page

Other font styles liked:
• same fonts of http://www.ryntholders.com/

Requirements
Must have
• - Very mobile friendly.
• - One paged with some inner pages.
• - Animated sticky header .
• - Member login area for e-trade.
• - Support RTL language.
• - HTML & CSS.
Nice to have
• Slider , some Qatari theme,
• i like the video inside the home page
• ex :http://www.ryntholders.com/

```html
<!DOCTYPE html>
<html lang="en">
<head>
<meta charset="utf-8">
<title>OKDM — Brokers at Pelorn Exchange</title>
<link href="https://fonts.googleapis.com/css2?family=Open+Sans:wght@400;600;700;800&display=swap" rel="stylesheet">
<style>
:root{
  --red:#8c1d1d;
  --red-bright:#a82424;
  --ink:#1f1f1f;
  --muted:#6b6b6b;
  --line:#d6d6d6;
  --paper:#ffffff;
  --mist:#ececec;
  --night:#141016;
  --footer:#0d0d0d;
  --green:#2f9e44;
}
*{box-sizing:border-box;margin:0;padding:0}
html,body{width:1200px;height:5279px;overflow:hidden}
body{position:relative;font-family:"Open Sans",Arial,sans-serif;color:var(--ink);background:var(--mist)}
.block{position:absolute;left:0;width:1200px}
h2.section-title{font-size:30px;font-weight:800;letter-spacing:.5px;color:var(--ink)}
p.body{font-size:13px;line-height:1.75;color:var(--muted)}
.btn-red{display:inline-block;background:var(--red);color:#fff;font-size:12px;font-weight:700;padding:10px 18px;letter-spacing:.5px}

/* hero */
.hero{top:0;height:700px;background:linear-gradient(180deg,#1a1522 0%,#2b2233 40%,#4a2c33 70%,#1c1418 100%)}
.hero-photo{position:absolute;inset:0;background:radial-gradient(ellipse at 55% 70%,rgba(210,140,90,.35),transparent 60%),linear-gradient(180deg,rgba(20,15,25,.2),rgba(20,15,25,.6))}
.topbar{position:absolute;top:30px;right:60px;display:flex;gap:8px}
.topbar span{font-size:10px;font-weight:700;color:#fff;padding:5px 10px}
.topbar .trade{background:var(--red)}
.topbar .lang{background:rgba(255,255,255,.15)}
.brand{position:absolute;top:42px;left:70px;display:flex;align-items:center;gap:12px;color:#fff;font-size:34px;font-weight:800}
.brand i{width:36px;height:36px;border:3px solid #fff;border-radius:50%}
.nav{position:absolute;top:80px;right:60px;display:flex;gap:30px}
.nav a{color:#fff;font-size:11px;font-weight:700;text-decoration:none;letter-spacing:.4px}
.play{position:absolute;top:250px;left:563px;width:74px;height:74px;border:3px solid rgba(255,255,255,.7);border-radius:50%}
.hero-title{position:absolute;top:345px;width:100%;text-align:center;color:#fff}
.hero-title h1{font-size:38px;font-weight:800;letter-spacing:1px}
.hero-title p{font-size:30px;font-weight:600;margin-top:6px}
.arrow{position:absolute;top:350px}

/* who we are */
.who{top:590px;height:720px;background:var(--paper);clip-path:polygon(0 70px,390px 0,1200px 90px,1200px 100%,0 100%)}
.who-photo{position:absolute;left:640px;top:0;width:560px;height:660px;background:linear-gradient(170deg,#24355f 0%,#3d4f86 35%,#c98e55 75%,#2a2530 100%);clip-path:polygon(0 45px,560px 90px,560px 100%,0 100%)}
.who .text{position:absolute;left:158px;top:155px;width:420px}
.who .lead{margin-top:30px}
.who .cols{display:flex;gap:22px;margin-top:22px}
.who .cols p{font-size:11px;line-height:1.7;color:var(--muted)}
.who .btn-red{margin-top:28px}

/* what we do */
.what{top:1250px;height:430px;background:var(--mist);clip-path:polygon(0 20px,640px 0,1200px 30px,1200px 100%,0 100%)}
.what h2{position:absolute;left:158px;top:118px}
.what .lead{position:absolute;left:158px;top:205px;width:350px;font-style:italic;font-size:13px;line-height:1.7;color:var(--muted)}
.what .side{position:absolute;left:558px;top:110px;width:484px}
.what .side p{font-size:11px;line-height:1.7;color:var(--muted)}
.what .btn-red{margin-top:14px}

/* city band */
.city{top:1600px;height:580px;background:linear-gradient(100deg,#e39a52 0%,#b97c55 22%,#6f7184 48%,#3f4d68 75%,#2e3a52 100%)}

/* services */
.services{top:2010px;height:720px;background:#eeeeee;clip-path:polygon(0 155px,390px 0,1200px 150px,1200px 100%,0 100%)}
.svc{position:absolute;top:243px;width:222px;height:227px;display:flex;align-items:center;justify-content:center}
.svc.active{background:var(--red)}
.svc .ring{width:190px;height:190px;border-radius:50%;border:5px solid var(--red);display:flex;align-items:center;justify-content:center;background:#fff}
.svc.active .ring{border-color:#fff;background:transparent}
.divider{position:absolute;top:255px;width:1px;height:205px;background:var(--line)}

/* news */
.news{top:2690px;height:640px;background:var(--paper);clip-path:polygon(0 0,1200px 60px,1200px 100%,0 100%)}
.news h2{position:absolute;left:158px;top:90px}
.card{position:absolute;top:160px;width:272px}
.card .thumb{height:180px}
.card h3{font-size:15px;font-weight:700;line-height:1.4;margin-top:18px}
.card p{font-size:11px;line-height:1.7;color:var(--muted);margin-top:12px}
.card .date{margin-top:12px;font-size:13px;font-weight:700;color:var(--red)}
.card .date::before{content:"";display:inline-block;width:34px;height:2px;background:var(--red);vertical-align:middle;margin-right:8px}

/* testimonials */
.voices{top:3260px;height:620px;background:linear-gradient(180deg,#1d1a22,#2a2530 50%,#15121a);clip-path:polygon(0 70px,540px 0,1200px 60px,1200px 100%,0 100%)}
.voice{position:absolute;top:320px;width:200px}
.voice p{font-size:11px;line-height:1.7;color:#c9c9c9}
.voice .who-said{margin-top:18px;font-size:12px;font-weight:700;color:#fff;letter-spacing:.5px}
.dots{position:absolute;top:520px;left:578px;display:flex;gap:6px}
.dots i{width:8px;height:8px;border-radius:50%;background:#fff;opacity:.5}
.dots i:first-child{opacity:1}

/* market data */
.market{top:3820px;height:900px;background:var(--paper);clip-path:polygon(0 0,600px 60px,1200px 0,1200px 100%,0 100%)}
.market h2{position:absolute;left:158px;top:90px}
.market .intro{position:absolute;left:158px;top:140px;width:884px;font-size:11px;line-height:1.7;color:var(--muted)}
.status{position:absolute;left:158px;top:245px;width:884px;height:72px;border:1px solid var(--line);border-radius:8px;display:flex;align-items:center;justify-content:space-between;padding:0 20px;white-space:nowrap}
.status .cell b{display:block;font-size:15px;font-weight:700}
.status .cell small{font-size:9px;color:var(--muted)}
.status .tag{font-size:9px;font-weight:800;line-height:1.3}
.status .tag em{font-style:normal;color:var(--red)}
.status .up{color:var(--green)}
.sub-title{position:absolute;top:380px;font-size:16px;font-weight:800;color:var(--red)}
.chart{position:absolute;left:158px;top:440px;width:415px;height:405px;background:#fff;box-shadow:0 0 0 1px var(--line)}
.chart .cap{font-size:8px;color:var(--muted);padding:18px 22px 8px}
.tabs{display:flex;margin:0 22px;border-bottom:1px solid var(--line)}
.tabs span{flex:1;text-align:center;font-size:9px;font-weight:700;padding:6px 0}
.tabs span.on{border-bottom:2px solid var(--red);color:var(--red)}
.movers{position:absolute;left:623px;top:420px;width:419px}
.movers .mtabs{display:flex;gap:26px;font-size:11px;font-weight:800;padding-bottom:10px;border-bottom:2px solid var(--ink)}
.movers table{width:100%;border-collapse:collapse;font-size:10px;margin-top:6px}
.movers th{font-weight:600;color:var(--muted);text-align:left;padding:8px 10px;background:#f3f3f3}
.movers td{padding:9px 10px;border-bottom:1px solid #eee}
.movers td.sym{color:var(--red);font-weight:700}
.movers tr.hl td{background:#f6e5e5}
.movers td.chg{color:var(--green);font-weight:700}

/* skyline */
.skyline{top:4640px;height:400px;background:linear-gradient(180deg,rgba(236,236,236,0) 0%,#d9b3b3 55%,#a34a4a 100%)}

/* footer */
.footer{top:5033px;height:246px;background:var(--footer);color:#fff;text-align:center}
.footer .brand-foot{position:absolute;top:32px;left:0;width:100%;display:flex;justify-content:center;align-items:center;gap:10px;font-size:26px;font-weight:800}
.footer .brand-foot i{width:28px;height:28px;border:3px solid #fff;border-radius:50%}
.footer nav{position:absolute;top:108px;width:100%;font-size:11px;font-weight:700;letter-spacing:.4px}
.footer nav span{margin:0 10px}
.footer .legal{position:absolute;top:135px;width:100%;font-size:8px;color:#aaa}
.social{position:absolute;top:160px;left:0;width:100%;display:flex;justify-content:center;gap:8px}
.social i{width:22px;height:22px;border:1px solid #fff;border-radius:50%}
</style>
</head>
<body>

<header class="block hero">
  <div class="hero-photo" role="img" aria-label="Night skyline of the city's towers lit over the bay"></div>
  <div class="topbar"><span class="trade">IPO &amp; TRADE</span><span class="lang">ENGLISH ▾</span></div>
  <div class="brand"><i></i>OKDM</div>
  <nav class="nav"><a>OKDM</a><a>FINANCIAL SERVICE</a><a>NEWS</a><a>MARKET TOOL</a><a>FORMS</a><a>CAREERS</a><a>CONTACT US</a></nav>
  <svg class="play" viewBox="0 0 74 74"><path d="M30 24 L50 37 L30 50Z" fill="rgba(255,255,255,.8)"/></svg>
  <div class="hero-title"><h1>BROKERS AT PELORN EXCHANGE</h1><p>We are a financial services company</p></div>
  <svg class="arrow" style="left:36px" width="24" height="44" viewBox="0 0 24 44"><path d="M20 4 L4 22 L20 40" stroke="#fff" stroke-width="3" fill="none"/></svg>
  <svg class="arrow" style="right:36px" width="24" height="44" viewBox="0 0 24 44"><path d="M4 4 L20 22 L4 40" stroke="#fff" stroke-width="3" fill="none"/></svg>
</header>

<section class="block who">
  <div class="who-photo" role="img" aria-label="Glass towers of the business district at dusk"></div>
  <div class="text">
    <h2 class="section-title">WHO WE ARE</h2>
    <p class="body lead">Sed ut perspiciatis unde omnis iste natus error sit voluptatem accusantium doloremque laudantium, totam rem aperiam, eaque ipsa quae ab illo inventore veritatis et quasi architecto beatae vitae dicta sunt.</p>
    <div class="cols">
      <p>Sed ut perspiciatis unde omnis iste natus error sit voluptatem accusantium doloremque laudantium, totam rem aperiam, eaque ipsa quae ab illo inventore veritatis et quasi architecto beatae vitae dicta sunt explicabo. Nemo enim ipsam voluptatem quia voluptas sit aspernatur.</p>
      <p>Sed ut perspiciatis unde omnis iste natus error sit voluptatem accusantium doloremque laudantium, totam rem aperiam, eaque ipsa quae ab illo inventore veritatis et quasi architecto beatae vitae dicta sunt explicabo. Nemo enim ipsam voluptatem quia voluptas sit aspernatur.</p>
    </div>
    <span class="btn-red">ABOUT OKDM</span>
  </div>
</section>

<section class="block what">
  <h2 class="section-title">WHAT WE DO</h2>
  <p class="lead">Sed ut perspiciatis unde omnis iste natus error sit voluptatem accusantium doloremque laudantium, totam rem aperiam, eaque ipsa quae ab illo inventore veritatis et quasi architecto beatae vitae dicta sunt explicabo.</p>
  <div class="side">
    <p>Sed ut perspiciatis unde omnis iste natus error sit voluptatem accusantium doloremque laudantium, totam rem aperiam, eaque ipsa quae ab illo inventore veritatis et quasi architecto beatae vitae dicta sunt explicabo. Nemo enim ipsam voluptatem quia voluptas sit aspernatur aut odit aut fugit, sed quia consequuntur magni dolores eos qui ratione voluptatem sequi nesciunt. Neque porro quisquam est, qui dolorem ipsum quia dolor sit amet, consectetur, adipisci velit, sed quia non numquam eius modi tempora incidunt ut labore et dolore magnam aliquam quaerat voluptatem.</p>
    <span class="btn-red">READ MORE</span>
  </div>
</section>

<section class="block city" role="img" aria-label="Panorama of the city skyline at sunset"></section>

<section class="block services">
  <div class="svc active" style="left:158px"><div class="ring">
    <svg width="90" height="70" viewBox="0 0 90 70"><rect x="8" y="18" width="60" height="38" rx="4" fill="none" stroke="#fff" stroke-width="4" transform="rotate(-12 38 37)"/><rect x="22" y="14" width="60" height="38" rx="4" fill="none" stroke="#fff" stroke-width="4"/><line x1="22" y1="26" x2="82" y2="26" stroke="#fff" stroke-width="6"/></svg>
  </div></div>
  <div class="divider" style="left:405px"></div>
  <div class="svc" style="left:410px"><div class="ring">
    <svg width="50" height="80" viewBox="0 0 50 80"><rect x="4" y="4" width="42" height="72" rx="6" fill="none" stroke="#8c1d1d" stroke-width="5"/><line x1="4" y1="62" x2="46" y2="62" stroke="#8c1d1d" stroke-width="4"/><circle cx="25" cy="69" r="3" fill="#8c1d1d"/></svg>
  </div></div>
  <div class="divider" style="left:630px"></div>
  <div class="svc" style="left:620px"><div class="ring">
    <svg width="80" height="70" viewBox="0 0 80 70"><rect x="6" y="48" width="12" height="18" fill="#8c1d1d"/><rect x="24" y="38" width="12" height="28" fill="#8c1d1d"/><rect x="42" y="28" width="12" height="38" fill="#8c1d1d"/><path d="M6 34 L34 16 L46 22 L70 6" stroke="#8c1d1d" stroke-width="5" fill="none"/><path d="M60 4 L74 4 L72 18" stroke="#8c1d1d" stroke-width="5" fill="none"/></svg>
  </div></div>
  <div class="divider" style="left:850px"></div>
  <div class="svc" style="left:840px"><div class="ring">
    <svg width="90" height="64" viewBox="0 0 90 64"><rect x="14" y="6" width="62" height="42" rx="3" fill="none" stroke="#8c1d1d" stroke-width="5"/><path d="M4 54 H86 L80 60 H10Z" fill="#8c1d1d"/><path d="M22 38 L36 24 L46 32 L66 14" stroke="#8c1d1d" stroke-width="4" fill="none"/></svg>
  </div></div>
</section>

<section class="block news">
  <h2 class="section-title">LATEST MARKET NEWS</h2>
  <article class="card" style="left:158px">
    <div class="thumb" role="img" aria-label="Visitors walking along the waterfront promenade" style="background:linear-gradient(180deg,#a9c3d8,#d8c6a3 60%,#8e7d68)"></div>
    <h3>Sed ut perspiciatis unde omniste natuerror sit voluptat accusam.</h3>
    <p>Sed ut perspiciatis unde omnis iste natus error sit voluptatem accusantium doloremque laudantium totam rem aperiam, eaque ipsa quae ab illo inventore quasi architecto beatae vitae dicta.</p>
    <div class="date">25 January, 2017</div>
  </article>
  <article class="card" style="left:461px">
    <div class="thumb" role="img" aria-label="Office towers under a blue sky" style="background:linear-gradient(180deg,#7aa3cf,#b9c8d8 55%,#6b7888)"></div>
    <h3>Sed ut perspiciatis unde nis iste natuerror sit voluptat accusam.</h3>
    <p>Sed ut perspiciatis unde omnis iste natus error sit voluptatem accusantium doloremque laudantium totam rem aperiam, eaque ipsa quae ab illo inventore quasi architecto beatae vitae dicta.</p>
    <div class="date">25 January, 2017</div>
  </article>
  <article class="card" style="left:767px">
    <div class="thumb" role="img" aria-label="Traditional boats moored in the harbour at sunset" style="background:linear-gradient(180deg,#e2b27a,#c98b5b 50%,#4f5f6e)"></div>
    <h3>Sed ut perspiciatis unde omniste natuerror sit voluptat accusam.</h3>
    <p>Sed ut perspiciatis unde omnis iste natus error sit voluptatem accusantium doloremque laudantium totam rem aperiam, eaque ipsa quae ab illo inventore quasi architecto beatae vitae dicta.</p>
    <div class="date">25 January, 2017</div>
  </article>
</section>

<section class="block voices" role="img" aria-label="Client testimonials over a darkened night skyline">
  <div class="voice" style="left:158px"><p>Sed ut perspiciatis unde omnis iste natus error sit voluptatem accusantium doloremque laudantium totam rem aperiam eaque ipsa quae ab illo inventore veritatis et quasi architecto beatae vitae dicta sunt.</p><div class="who-said">— MARA T. QUILL</div></div>
  <div class="voice" style="left:387px"><p>Sed ut perspiciatis unde omnis iste natus error sit voluptatem accusantium doloremque laudantium totam rem aperiam eaque ipsa quae ab illo inventore veritatis et quasi architecto beatae vitae dicta sunt.</p><div class="who-said">— MARA T. QUILL</div></div>
  <div class="voice" style="left:626px"><p>Sed ut perspiciatis unde omnis iste natus error sit voluptatem accusantium doloremque laudantium totam rem aperiam eaque ipsa quae ab illo inventore veritatis et quasi architecto beatae vitae dicta sunt.</p><div class="who-said">— MARA T. QUILL</div></div>
  <div class="voice" style="left:845px"><p>Sed ut perspiciatis unde omnis iste natus error sit voluptatem accusantium doloremque laudantium totam rem aperiam eaque ipsa quae ab illo inventore veritatis et quasi architecto beatae vitae dicta sunt.</p><div class="who-said">— MARA T. QUILL</div></div>
  <div class="dots"><i></i><i></i><i></i><i></i></div>
</section>

<section class="block market">
  <h2 class="section-title">MARKET DATA</h2>
  <p class="intro">Sed ut perspiciatis unde omnis iste natus error sit voluptatem accusantium doloremque laudantium, totam rem aperiam, eaque ipsa quae ab illo inventore veritatis et quasi architecto beatae vitae dicta sunt explicabo. Nemo enim ipsam voluptatem quia voluptas sit aspernatur aut odit aut fugit, sed quia consequuntur magni dolores eos qui ratione.</p>
  <div class="status">
    <svg width="26" height="26" viewBox="0 0 26 26"><circle cx="13" cy="13" r="11" fill="none" stroke="#8c1d1d" stroke-width="3"/><rect x="9" y="9" width="8" height="8" fill="#8c1d1d"/></svg>
    <div class="tag">MARKET STATUS<br><em>POST TRADING</em></div>
    <div class="cell"><b class="up">▲ 20,046.60</b><small>Index</small></div>
    <div class="cell"><b class="up">▲ 20.00 (+0.10%)</b><small>Change</small></div>
    <div class="cell"><b>10,000</b><small>Trades</small></div>
    <div class="cell"><b>15,130</b><small>Volume</small></div>
    <div class="cell"><b>1,524,380,159.00</b><small>Value</small></div>
    <div class="tag">LAST UPDATED<br><em>FEB 08, 2017 02:51:27 PM</em></div>
  </div>

  <div class="sub-title" style="left:158px">INDEX CHART</div>
  <div class="sub-title" style="left:623px">MARKET MOVERS</div>

  <div class="chart">
    <div class="cap">TREVA 500 | 8:46 PM AT 02/10/2017</div>
    <div class="tabs"><span class="on">1D</span><span>1M</span><span>3M</span><span>6M</span><span>1Y</span><span>5Y</span><span>YTD</span></div>
    <svg width="415" height="320" viewBox="0 0 415 320">
      <defs><linearGradient id="areaFill" x1="0" y1="0" x2="0" y2="1"><stop offset="0" stop-color="#8c1d1d"/><stop offset="1" stop-color="#8c1d1d" stop-opacity=".08"/></linearGradient></defs>
      <line x1="22" y1="40" x2="330" y2="40" stroke="#bbb" stroke-dasharray="3 3"/>
      <text x="26" y="34" font-size="9" fill="#555" font-family="Open Sans,sans-serif">Previous Close 1900.00</text>
      <path d="M22 240 L60 200 L100 150 L140 95 L170 70 L330 70 L330 300 L22 300Z" fill="url(#areaFill)"/>
      <path d="M22 240 L60 200 L100 150 L140 95 L170 70 L330 70" stroke="#8c1d1d" stroke-width="2" fill="none"/>
      <rect x="336" y="62" width="50" height="16" fill="#8c1d1d"/>
      <text x="342" y="74" font-size="9" fill="#fff" font-family="Open Sans,sans-serif">1905.00</text>
      <g font-size="9" fill="#777" font-family="Open Sans,sans-serif">
        <text x="342" y="130">1900.00</text><text x="342" y="180">1895.00</text><text x="342" y="230">1890.00</text><text x="342" y="280">1885.00</text>
      </g>
    </svg>
  </div>

  <div class="movers">
    <div class="mtabs"><span>TOP GAINERS</span><span>TOP DECLINERS</span><span>TOP ACTIVE</span></div>
    <table>
      <tr><th>&nbsp;</th><th>LAST</th><th>%CHG</th></tr>
      <tr class="hl"><td class="sym">TREVA 500</td><td>2248.00</td><td class="chg">0.12%</td></tr>
      <tr><td class="sym">ZARETH</td><td>2248.00</td><td class="chg">0.12%</td></tr>
      <tr><td class="sym">ZARETH</td><td>2248.00</td><td class="chg">0.12%</td></tr>
      <tr><td class="sym">OMBRIX 30</td><td>2248.00</td><td class="chg">0.12%</td></tr>
      <tr><td class="sym">^ TULVA</td><td>2248.00</td><td class="chg">0.12%</td></tr>
      <tr><td class="sym">^ KESHRO</td><td>2248.00</td><td class="chg">0.12%</td></tr>
      <tr><td class="sym">^ MIRDAN</td><td>2248.00</td><td>0%</td></tr>
      <tr><td class="sym">^ VORLIK</td><td>2248.00</td><td class="chg">0.12%</td></tr>
      <tr><td class="sym">^ QUELTA</td><td>2248.00</td><td class="chg">0.12%</td></tr>
    </table>
  </div>
</section>

<div class="block skyline" role="img" aria-label="Drawn skyline of the city's landmark towers in deep red"></div>

<footer class="block footer">
  <div class="brand-foot"><i></i>OKDM</div>
  <nav><span>OKDM</span>|<span>FINANCIAL SERVICE</span>|<span>NEWS</span>|<span>MARKET TOOL</span>|<span>CAREERS</span>|<span>CONTACT US</span></nav>
  <div class="legal">©2017. All Rights Reserved | OKDM Pelorn | Copyright, Legal and Privacy Statement, Disclaimers and Legal Information</div>
  <div class="social"><i></i><i></i><i></i><i></i><i></i></div>
</footer>

</body>
</html>
```